Please create a custom business card for 'Adventures beyond any map'. The logo is attached to this brief.

Here is the link to the logo project : http://work.plumvessel.example/task.aspx?id=319207

Questions can be posted on the Discussion Board.

```html
<!DOCTYPE html>
<html lang="en">
<head>
<meta charset="utf-8">
<title>Adventures beyond any map — business card</title>
<link href="https://fonts.googleapis.com/css2?family=Open+Sans:wght@400;600;700&display=swap" rel="stylesheet">
<style>
  :root{
    --brand-red:#e3201f;
    --deep-red:#b9141a;
    --ink:#1d1d1d;
    --mid-grey:#8a8a8a;
    --light-grey:#cfcfcf;
    --card-white:#fbfbfb;
    --backdrop:#3a3a3a;
  }
  *{margin:0;padding:0;box-sizing:border-box}
  html,body{width:1200px;height:676px;overflow:hidden}
  body{
    background:var(--backdrop);
    font-family:"Open Sans",Arial,sans-serif;
    position:relative;
  }
  .card{
    position:absolute;
    top:190px;
    width:520px;height:297px;
    overflow:hidden;
    box-shadow:0 10px 24px rgba(0,0,0,.45);
  }

  /* Back of card */
  .card-back{left:60px;background:var(--brand-red)}
  .card-back .pattern-area{
    position:absolute;inset:0;
    background:linear-gradient(135deg,var(--brand-red) 0%,var(--deep-red) 50%,var(--brand-red) 100%);
  }
  .card-back .wordmark{
    position:absolute;left:0;right:0;top:92px;
    text-align:center;
    font-weight:700;font-size:92px;letter-spacing:2px;
    color:#fff;line-height:1;
  }
  .card-back .web{
    position:absolute;right:26px;bottom:20px;
    color:#fff;font-size:15px;font-weight:400;
  }

  /* Front of card */
  .card-front{left:620px;background:var(--card-white)}
  .brand{
    position:absolute;left:36px;top:38px;
    display:flex;align-items:center;gap:12px;
  }
  .brand-square{width:44px;height:44px;background:var(--brand-red)}
  .brand-name{
    font-weight:700;font-size:62px;line-height:1;
    color:var(--brand-red);letter-spacing:1px;
  }
  .rule{
    position:absolute;left:150px;top:120px;
    display:flex;height:4px;width:330px;
  }
  .rule span{height:100%}
  .rule .r1{width:42%;background:var(--brand-red)}
  .rule .r2{width:20%;background:var(--mid-grey)}
  .rule .r3{width:20%;background:var(--light-grey)}
  .rule .r4{width:18%;background:var(--ink)}

  .contacts{
    position:absolute;left:34px;top:122px;
    list-style:none;font-size:12px;color:var(--ink);line-height:16px;
  }
  .contacts li{display:flex;align-items:center;gap:8px}
  .contacts svg{width:9px;height:9px;flex:none}

  .person{
    position:absolute;right:40px;top:138px;text-align:right;
  }
  .person .name{font-size:20px;color:var(--brand-red);line-height:1.1}
  .person .role{font-size:12px;color:var(--ink);margin-bottom:6px}
  .person .address{font-size:12px;color:var(--brand-red);line-height:15px;padding-right:16px}
  .pin{position:absolute;right:40px;top:200px;width:10px;height:12px}
  .person-bar{
    position:absolute;right:40px;top:222px;
    width:150px;height:4px;background:var(--ink);
  }

  .swoosh{position:absolute;left:0;bottom:0;width:520px;height:297px}
</style>
</head>
<body>

  <section class="card card-back" aria-label="Business card back">
    <div class="pattern-area" role="img" aria-label="Repeating cube pattern in red tones"></div>
    <div class="wordmark">roamly</div>
    <div class="web">www.roamly.example</div>
  </section>

  <section class="card card-front" aria-label="Business card front">
    <svg class="swoosh" viewBox="0 0 520 297" preserveAspectRatio="none" aria-hidden="true">
      <path d="M0 198 C130 222 260 258 520 264 L520 297 L0 297 Z" fill="var(--brand-red)"/>
      <path d="M0 206 C135 232 265 266 520 271 L520 297 L0 297 Z" fill="#fff"/>
      <path d="M0 214 C140 242 270 274 520 279 L520 297 L0 297 Z" fill="var(--mid-grey)"/>
      <path d="M0 222 C150 252 280 282 520 286 L520 297 L0 297 Z" fill="var(--brand-red)"/>
      <path d="M0 252 C120 274 300 292 520 294 L520 297 L0 297 Z" fill="var(--deep-red)"/>
    </svg>

    <div class="brand">
      <div class="brand-square"></div>
      <div class="brand-name">roamly</div>
    </div>
    <div class="rule"><span class="r1"></span><span class="r2"></span><span class="r3"></span><span class="r4"></span></div>

    <ul class="contacts">
      <li><svg viewBox="0 0 10 10"><rect x="2" y="0" width="6" height="10" rx="1" fill="var(--brand-red)"/></svg>0987 654 321</li>
      <li><svg viewBox="0 0 10 10"><rect x="0.5" y="0.5" width="9" height="9" fill="none" stroke="var(--ink)"/></svg>0987 654 321</li>
      <li><svg viewBox="0 0 10 10"><rect x="0" y="2" width="10" height="7" fill="var(--brand-red)"/><path d="M0 2 L5 6 L10 2" stroke="#fff" fill="none"/></svg>hello@roamly.example</li>
      <li><svg viewBox="0 0 10 10"><circle cx="5" cy="5" r="4.3" fill="none" stroke="var(--brand-red)" stroke-width="1.2"/><path d="M1 5 H9 M5 1 V9" stroke="var(--brand-red)"/></svg>www.roamly.example</li>
    </ul>

    <div class="person">
      <div class="name">your name</div>
      <div class="role">designation</div>
      <div class="address">address (street address<br>suite number, city, state, zip</div>
    </div>
    <svg class="pin" viewBox="0 0 10 12" aria-hidden="true"><path d="M5 12 C2 8 0 6 0 4 A5 5 0 0 1 10 4 C10 6 8 8 5 12 Z" fill="var(--ink)"/><circle cx="5" cy="4" r="1.6" fill="#fff"/></svg>
    <div class="person-bar"></div>
  </section>

</body>
</html>
```